Consulting firm needs an infographic

The consulting we do needs a very graphic and understandable way to have perspective clients get exactly where we can help their company grow. I designed something that needs a lot of spice for it to look professional and relatable to them. This is being created to be used on a business card, as well as on posters, and social media.

```html
<!DOCTYPE html>
<html lang="en">
<head>
<meta charset="utf-8">
<title>Your Company – Growth Map</title>
<link rel="stylesheet" href="https://fonts.googleapis.com/css2?family=Archivo:wght@800;900&display=swap">
<style>
  :root{
    --bg-core:#3a3b3d;
    --bg-edge:#0e0f10;
    --white:#ffffff;
    --blue:#0892d8;
    --blue-ring:#3db9e6;
    --green:#84c129;
    --teal:#0fcf91;
    --yellow:#f5c300;
    --pink:#d81f84;
  }
  html,body{margin:0;padding:0;width:1200px;height:840px;overflow:hidden;background:var(--bg-edge);}
  .canvas{display:block;width:1200px;height:840px;}
  .backdrop-fill{fill:url(#backdrop);}
  .label{font-family:"Archivo",sans-serif;font-weight:800;fill:var(--white);font-size:22px;letter-spacing:.4px;}
  .title{font-family:"Archivo",sans-serif;font-weight:900;fill:var(--white);font-size:68px;}
  .hub-label{font-family:"Archivo",sans-serif;font-weight:800;fill:var(--white);font-size:20px;}
  .brand-name{font-family:"Archivo",sans-serif;font-weight:800;fill:var(--white);font-size:30px;}
  .ring{fill:none;stroke-width:11;}
  .ring-inner{fill:none;stroke:var(--white);stroke-width:2;}
  .hub-outer{fill:var(--white);}
  .ring--blue{stroke:var(--blue-ring);}
  .ring--green{stroke:var(--green);}
  .ring--teal{stroke:var(--teal);}
  .ring--yellow{stroke:var(--yellow);}
  .ring--pink{stroke:var(--pink);}
  .hub--blue{fill:var(--blue);}
  .hub--teal{fill:var(--teal);}
  .icon{fill:none;stroke-width:1.6;stroke-linecap:round;stroke-linejoin:round;}
  .icon--blue{stroke:var(--blue);color:var(--blue);}
  .icon--white{stroke:var(--white);}
  .icon--green{stroke:var(--green);}
  .icon--yellow{stroke:var(--yellow);}
  .icon--pink{stroke:var(--pink);}
  .arrow{fill:none;stroke-width:3;stroke-linecap:round;stroke-linejoin:round;}
  .arrow--blue{stroke:var(--blue-ring);}
  .arrow--teal{stroke:var(--teal);}
  .arrow--yellow{stroke:var(--yellow);stroke-width:2;}
  .arrow--green{stroke:var(--green);stroke-width:2;}
  .arrow--pink{stroke:var(--pink);stroke-width:2;}
  .brand-dot{fill:none;stroke:var(--green);stroke-width:5;}
</style>
</head>
<body>
<svg class="canvas" viewBox="0 0 1200 840" xmlns="http://www.w3.org/2000/svg">
  <defs>
    <radialGradient id="backdrop" cx="50%" cy="45%" r="70%">
      <stop offset="0" stop-color="var(--bg-core)"/>
      <stop offset="1" stop-color="var(--bg-edge)"/>
    </radialGradient>
    <symbol id="i-team" viewBox="0 0 24 24"><circle cx="12" cy="8" r="3"/><circle cx="5" cy="10" r="2.2"/><circle cx="19" cy="10" r="2.2"/><path d="M6 20c0-4 3-6 6-6s6 2 6 6"/><path d="M1 19c0-3 2-5 4-5M23 19c0-3-2-5-4-5"/></symbol>
    <symbol id="i-pin" viewBox="0 0 24 24"><path d="M12 22s-7-7-7-12a7 7 0 0 1 14 0c0 5-7 12-7 12z"/><rect x="9" y="8" width="6" height="4.5" rx="1"/><path d="M10.5 8V7h3v1"/></symbol>
    <symbol id="i-cycle" viewBox="0 0 24 24"><circle cx="12" cy="12" r="3"/><circle cx="12" cy="12" r="5.5" stroke-dasharray="2.2 1.4"/><path d="M3 12a9 9 0 0 1 15-6.7M21 12a9 9 0 0 1-15 6.7"/><path d="M18 2v3.5h-3.5M6 22v-3.5h3.5"/></symbol>
    <symbol id="i-boxes" viewBox="0 0 24 24"><rect x="8" y="2" width="8" height="7"/><rect x="3" y="9" width="9" height="9"/><rect x="12" y="9" width="9" height="9"/><path d="M1 20h22M3 22h2M19 22h2M7 12h2M16 12h2M11 4h2"/></symbol>
    <symbol id="i-exec" viewBox="0 0 24 24"><rect x="1" y="6" width="15" height="11" rx="1"/><path d="M4 14v-2M7 14v-4M10 14V9M13 14v-3M5 20h7M8.5 17v3"/><circle cx="19" cy="5" r="3"/><circle cx="18" cy="13" r="2.2"/><path d="M14 22c0-3 2-5 4-5s4 2 4 5"/></symbol>
    <symbol id="i-globe" viewBox="0 0 24 24"><circle cx="11" cy="11" r="8"/><path d="M3 11h16M11 3c3 3 3 13 0 16M11 3c-3 3-3 13 0 16"/><rect x="15" y="17" width="7" height="5"/><path d="M19 2l3 3-4 1z"/></symbol>
    <symbol id="i-store" viewBox="0 0 24 24"><path d="M3 8l2-5h14l2 5z"/><path d="M3 8c0 2 4 2 4 0 0 2 5 2 5 0 0 2 5 2 5 0 0 2 4 2 4 0"/><rect x="4" y="10" width="16" height="11"/><rect x="8" y="13" width="8" height="4"/><path d="M4 21h16"/></symbol>
    <symbol id="i-hand" viewBox="0 0 24 24"><circle cx="14" cy="7" r="3"/><circle cx="14" cy="7" r="5.5" stroke-dasharray="2 1.5"/><path d="M2 19l4-4h5l4 1 5-3"/><path d="M2 19l2 3"/></symbol>
    <symbol id="i-coins" viewBox="0 0 24 24"><ellipse cx="8" cy="5" rx="6" ry="2.5"/><path d="M2 5v12c0 1.5 3 2.5 6 2.5M14 5v5M2 9c0 1.5 3 2.5 6 2.5M2 13c0 1.5 3 2.5 6 2.5"/><circle cx="16" cy="16" r="6"/><path d="M18 13.5h-3a1.2 1.2 0 0 0 0 2.4h2a1.2 1.2 0 0 1 0 2.4h-3M16 12v8"/></symbol>
    <symbol id="i-shield" viewBox="0 0 24 24"><rect x="1" y="6" width="13" height="15" rx="1"/><circle cx="6" cy="12" r="2"/><path d="M3 18c0-2 1.5-3 3-3s3 1 3 3"/><path d="M16 3l6 2.5v6c0 4-3 7-6 9-3-2-6-5-6-9v-6z"/><circle cx="16" cy="10" r="2.5"/><path d="M15 10l1 1 1.5-2"/></symbol>
    <symbol id="i-growth" viewBox="0 0 24 24"><path d="M1 22h22M4 22v-5h3v5M10 22v-8h3v8M16 22v-11h3v11"/><path d="M1 15c7-2 13-6 19-13M16 2h4v4"/></symbol>
  </defs>

  <rect class="backdrop-fill" width="1200" height="840"/>

  <!-- Title row -->
  <g class="title-row">
    <path class="arrow arrow--blue" d="M345 110H292M302 101l-10 9 10 9"/>
    <text class="title" x="600" y="126" text-anchor="middle">Your Company</text>
    <path class="arrow arrow--teal" d="M858 108h54M902 99l10 9-10 9"/>
  </g>

  <!-- Rings -->
  <g class="ring-group">
    <circle class="ring ring--blue" cx="187" cy="327" r="157"/>
    <circle class="ring-inner" cx="187" cy="325" r="138"/>
    <circle class="ring ring--green" cx="600" cy="325" r="157"/>
    <circle class="ring-inner" cx="600" cy="325" r="138"/>
    <circle class="ring ring--teal" cx="1014" cy="325" r="157"/>
    <circle class="ring-inner" cx="1014" cy="325" r="138"/>
    <circle class="ring ring--yellow" cx="393" cy="624" r="157"/>
    <circle class="ring-inner" cx="393" cy="624" r="138"/>
    <circle class="ring ring--pink" cx="807" cy="624" r="157"/>
    <circle class="ring-inner" cx="807" cy="624" r="138"/>
  </g>

  <!-- Flow arrows -->
  <g class="flow-arrows">
    <path class="arrow arrow--blue" d="M282 462l20 25M302 479v8h-8" style="stroke-width:2"/>
    <path class="arrow arrow--yellow" d="M489 488l17-27M498 462l8-1 1 8"/>
    <path class="arrow arrow--green" d="M694 462l20 25M714 479v8h-8"/>
    <path class="arrow arrow--pink" d="M901 488l19-27M912 462l8-1 1 8"/>
  </g>

  <!-- Hubs -->
  <g class="hub hub-left">
    <circle class="hub-outer" cx="170" cy="131" r="96"/>
    <circle class="hub--blue" cx="170" cy="131" r="83"/>
    <use href="#i-boxes" class="icon icon--white" x="103" y="110" width="40" height="40"/>
    <text class="hub-label" x="146" y="126">Products</text>
    <text class="hub-label" x="146" y="151">/Services</text>
  </g>
  <g class="hub hub-right">
    <circle class="hub-outer" cx="1035" cy="133" r="96"/>
    <circle class="hub--teal" cx="1035" cy="133" r="83"/>
    <use href="#i-boxes" class="icon icon--white" x="967" y="113" width="40" height="40"/>
    <text class="hub-label" x="1011" y="129">Products</text>
    <text class="hub-label" x="1011" y="154">/Services</text>
  </g>

  <!-- Operations (left) -->
  <g class="topic topic--operations-in">
    <use href="#i-team" class="icon icon--blue" x="94" y="268" width="36" height="36"/>
    <text class="label" x="153" y="294">Workforce</text>
    <use href="#i-pin" class="icon icon--blue" x="97" y="315" width="32" height="32"/>
    <text class="label" x="153" y="337">Workplace</text>
    <use href="#i-cycle" class="icon icon--blue" x="99" y="356" width="32" height="32"/>
    <text class="label" x="153" y="380">Workflow</text>
  </g>

  <!-- Management (centre) -->
  <g class="topic topic--management">
    <use href="#i-exec" class="icon icon--green" x="499" y="264" width="42" height="42"/>
    <text class="label" x="553" y="281">Executive/</text>
    <text class="label" x="553" y="307">Administrative</text>
    <use href="#i-team" class="icon icon--green" x="502" y="315" width="38" height="38"/>
    <text class="label" x="551" y="340">Personnel</text>
    <use href="#i-globe" class="icon icon--green" x="503" y="356" width="36" height="36"/>
    <text class="label" x="551" y="380">Logistics</text>
  </g>

  <!-- Operations (right) -->
  <g class="topic topic--operations-out">
    <use href="#i-team" class="icon icon--blue" x="926" y="268" width="36" height="36"/>
    <text class="label" x="984" y="294">Workforce</text>
    <use href="#i-pin" class="icon icon--blue" x="929" y="315" width="32" height="32"/>
    <text class="label" x="984" y="337">Workplace</text>
    <use href="#i-cycle" class="icon icon--blue" x="932" y="356" width="32" height="32"/>
    <text class="label" x="984" y="380">Workflow</text>
  </g>

  <!-- Supply -->
  <g class="topic topic--supply">
    <use href="#i-store" class="icon icon--yellow" x="308" y="559" width="34" height="34"/>
    <text class="label" x="361" y="586">Vendors</text>
    <use href="#i-hand" class="icon icon--yellow" x="306" y="606" width="36" height="36"/>
    <text class="label" x="358" y="633">Resources</text>
    <use href="#i-coins" class="icon icon--yellow" x="311" y="656" width="34" height="34"/>
    <text class="label" x="358" y="682">Costs</text>
  </g>

  <!-- Market -->
  <g class="topic topic--market">
    <use href="#i-team" class="icon icon--pink" x="707" y="555" width="46" height="46"/>
    <text class="label" x="769" y="584">Customers</text>
    <use href="#i-shield" class="icon icon--pink" x="707" y="606" width="40" height="40"/>
    <text class="label" x="768" y="632">Identity &amp; B&amp;M</text>
    <use href="#i-growth" class="icon icon--pink" x="705" y="651" width="46" height="46"/>
    <text class="label" x="768" y="686">Revenue</text>
  </g>

  <!-- Brand -->
  <g class="brand">
    <circle class="brand-dot" cx="1078" cy="706" r="18"/>
    <text class="brand-name" x="1079" y="760" text-anchor="middle">Growfield</text>
  </g>
</svg>
</body>
</html>
```